Business Card Design

I am a criminologist running a research and consultancy business on my own (PKConsultants)
I specialise in looking at fraud and other white-collar crimes. Also governance issues..
I would like a professional business card that would be appropriate both in the academic and business sector as I straddle both sectors. Normal shape - not square.
I am interested in seeing border Word Cloud type projects - black on white or white on black..
Example key words would be fraud, research, qualitative, interviews, quantitative, white-collar, reports, government, surveys, sample, governance, assurance, crime, offenders, prison etc (I can provide a full list if this is the option I go for). I also like Word Cloud borders as attached.
I am also interested in seeing other style business cards. Preferably one colour, plus black and white.
In particular I like black backgrounds with coloured words etc - colours like lime green are good.
I also like blues - especially teal if a traditional white background is chosen.
I don't have a logo - unless anyone can think of anything that's particularly appropriate.
Graphics can be used but they would be simple and stylish (dots, squares, lines, curves etc)
I would like the design to translate simply for a header for a website or blog.
My current website is www.pelling-hurst.com but is out of date in terms of what I do and design.
I have attached a number of things that have caught my eye and inspired me.
I have asked for a one-sided business card in the first instance - however if someone comes up with a good cloud design that might go on one side, I would consider a two-sided one.
Design can be landscape or portrait.
Kind Regards
Meg
Landscape
Contact Information for Business Card
PKConsultants
Dr Margery Pelling-Hurst, MSc, BSc, **
42 Brindle Wold
Ashbury, Staffordshire
KX27 4QD
+44(0)1620 482917
+44(0)7531 804152
www.pelling-hurst.com
margery@pelling-hurst.com

```html
<!DOCTYPE html>
<html lang="en">
<head>
<meta charset="utf-8">
<title>PKConsultants – Business Card</title>
<link href="https://fonts.googleapis.com/css2?family=Fira+Sans:wght@400;600;700&family=Lato:wght@400;700&display=swap" rel="stylesheet">
<style>
  :root {
    --page: #e6e4e1;
    --card: #353535;
    --card-deep: #2b2b2b;
    --ink-light: #ffffff;
    --ink-soft: #d9d9d9;
    --band: #f4f4f4;
    --ink-dark: #2e2e2e;
  }
  * { margin: 0; padding: 0; box-sizing: border-box; }
  html, body { width: 1200px; height: 900px; overflow: hidden; }
  body {
    background: var(--page);
    display: flex; align-items: center; justify-content: center;
  }
  .business-card {
    position: relative;
    width: 1050px; height: 600px;
    background: linear-gradient(160deg, var(--card) 0%, var(--card-deep) 100%);
    box-shadow: 0 14px 40px rgba(0,0,0,.25);
    overflow: hidden;
    color: var(--ink-light);
    font-family: "Lato", sans-serif;
  }
  .light-streaks { position: absolute; inset: 0; width: 100%; height: 100%; }
  .company-name {
    position: absolute; top: 78px; left: 0; width: 100%;
    text-align: center;
    padding-left: 120px;
    font-family: "Fira Sans", sans-serif;
    font-weight: 700; font-size: 66px; letter-spacing: 2px;
  }
  .person {
    position: absolute; left: 110px; top: 272px;
  }
  .person-name {
    display: flex; align-items: center; gap: 16px;
    font-family: "Fira Sans", sans-serif;
    font-weight: 700; font-size: 54px; letter-spacing: 1.5px;
  }
  .person-name svg { width: 36px; height: 40px; }
  .credentials {
    margin: 6px 0 0 80px;
    font-family: "Fira Sans", sans-serif;
    font-size: 20px; font-weight: 600; letter-spacing: 1px;
    color: var(--ink-soft);
  }
  .contact-list {
    position: absolute; left: 555px; top: 286px;
    list-style: none;
    font-size: 26px; line-height: 1.4; letter-spacing: 1px;
  }
  .contact-list li { display: flex; align-items: flex-start; gap: 18px; margin-bottom: 6px; }
  .contact-list svg { width: 24px; height: 28px; flex: none; margin-top: 4px; }
  .footer-band {
    position: absolute; left: 0; bottom: 0; width: 100%; height: 80px;
    background: var(--band);
    color: var(--ink-dark);
    font-family: "Fira Sans", sans-serif; font-size: 23px; letter-spacing: 1px;
  }
  .footer-band .email,
  .footer-band .website {
    position: absolute; top: 50%; transform: translateY(-50%);
    display: flex; align-items: center; gap: 14px;
  }
  .footer-band .email { left: 70px; }
  .footer-band .website { left: 560px; gap: 12px; }
  .footer-band svg { width: 26px; height: 22px; }
</style>
</head>
<body>
  <div class="business-card">
    <svg class="light-streaks" viewBox="0 0 1050 600" aria-hidden="true">
      <defs>
        <linearGradient id="streak-h" x1="0" x2="1" y1="0" y2="0">
          <stop offset="0" stop-color="#fff" stop-opacity="0"/>
          <stop offset=".45" stop-color="#fff" stop-opacity=".95"/>
          <stop offset="1" stop-color="#fff" stop-opacity="0"/>
        </linearGradient>
        <linearGradient id="streak-v" x1="0" x2="0" y1="0" y2="1">
          <stop offset="0" stop-color="#fff" stop-opacity="0"/>
          <stop offset=".5" stop-color="#fff" stop-opacity=".95"/>
          <stop offset="1" stop-color="#fff" stop-opacity="0"/>
        </linearGradient>
      </defs>
      <polygon points="20,168 1040,222 1040,226 20,171" fill="url(#streak-h)"/>
      <polygon points="520,12 1040,64 1040,66 520,14" fill="url(#streak-h)" opacity=".35"/>
      <polygon points="512,256 517,256 498,480 494,480" fill="url(#streak-v)"/>
    </svg>

    <h1 class="company-name">PKConsultants</h1>

    <div class="person">
      <div class="person-name">
        <svg viewBox="0 0 36 40" aria-hidden="true"><circle cx="18" cy="11" r="9" fill="#fff"/><path d="M2 40 Q2 23 18 23 Q34 23 34 40 Z" fill="#fff"/></svg>
        <span>Dr Margery</span>
      </div>
      <p class="credentials">MSc, BSc</p>
    </div>

    <ul class="contact-list">
      <li>
        <svg viewBox="0 0 24 28" aria-hidden="true"><path d="M12 1a9 9 0 0 0-9 9c0 7 9 17 9 17s9-10 9-17a9 9 0 0 0-9-9zm0 13a4 4 0 1 1 0-8 4 4 0 0 1 0 8z" fill="#fff"/></svg>
        <span>42 Brindle Wold Ashbury,<br>Wendlemere KX27 4QD</span>
      </li>
      <li>
        <svg viewBox="0 0 24 28" aria-hidden="true"><path d="M6 4l4 5-2 3c1 3 3 5 6 6l3-2 5 4-2 4C10 24 2 14 4 6z" fill="#fff"/></svg>
        <span>+44(0)1620 482917</span>
      </li>
      <li>
        <svg viewBox="0 0 24 28" aria-hidden="true"><path d="M6 4l4 5-2 3c1 3 3 5 6 6l3-2 5 4-2 4C10 24 2 14 4 6z" fill="#fff"/></svg>
        <span>+44(0)7531 804152</span>
      </li>
    </ul>

    <div class="footer-band">
      <span class="email">
        <svg viewBox="0 0 26 22" aria-hidden="true"><rect x="1" y="3" width="24" height="16" fill="none" stroke="#2e2e2e" stroke-width="2"/><path d="M1 3l12 9 12-9" fill="none" stroke="#2e2e2e" stroke-width="2"/></svg>
        margery@pelling-hurst.com
      </span>
      <span class="website">
        <svg viewBox="0 0 22 22" aria-hidden="true"><circle cx="11" cy="11" r="9.5" fill="none" stroke="#2e2e2e" stroke-width="2"/><ellipse cx="11" cy="11" rx="4" ry="9.5" fill="none" stroke="#2e2e2e" stroke-width="1.6"/><path d="M2 11h18M4 6h14M4 16h14" stroke="#2e2e2e" stroke-width="1.4"/></svg>
        www.pelling-hurst.com
      </span>
    </div>
  </div>
</body>
</html>
```